WEBSITE NEEDED FOR MY COMPANY CALLED BRAVERIDGE HOCKEY DEVELOPMENT

LOOKING FOR A WEBSITE TO MARKET AND SEEL MY HOCKEY DEVELOPMENT PROGRAMS.
NEEDS TO HAVE 5+ PAGES

Target Market(s)

YOUTH SPORTS

Industry/Entity Type

YOUTH ATHLETE DEVELOPMENT

Number of Pages Required

5+ page

Font styles to use
Sans Serif

Colors
0054AA
0677BA
7BADD7
CADEEF
E8F1F8

Requirements
Must have
• MAIN PAGE - SPIRNG PROGRAM PAGE - SUMMER PROGRAM PAGE - WINTER PAGE - TOURNAMENT PAGE
Nice to have
• FLASH
Should not have
• NOT SURE

```html
<!DOCTYPE html>
<html lang="en">
<head>
<meta charset="utf-8">
<title>Braveridge Hockey Development</title>
<link href="https://fonts.googleapis.com/css2?family=Orbitron:wght@500;700;900&family=Montserrat:wght@400;500;600;700&family=Roboto+Condensed:wght@700&display=swap" rel="stylesheet">
<style>
:root{
  --navy:#0f2740;
  --navy-deep:#0b1e33;
  --navy-bar:#102a45;
  --cyan:#2cb9ef;
  --cyan-soft:#5fcdf5;
  --ice:#eef3f8;
  --ice-2:#dfe8f1;
  --text:#2b3440;
  --muted:#5b6672;
  --white:#ffffff;
}
*{margin:0;padding:0;box-sizing:border-box}
html,body{width:1200px;height:4243px;overflow:hidden}
body{position:relative;background:var(--ice);font-family:"Montserrat",sans-serif;color:var(--text)}
.abs{position:absolute}
.display{font-family:"Orbitron",sans-serif;font-weight:700;letter-spacing:1px}
.condensed{font-family:"Roboto Condensed",sans-serif;font-weight:700}
.photo{position:absolute}
.btn-solid{position:absolute;background:linear-gradient(90deg,#3fc6f3,#22a9e6);color:#fff;font-weight:600;font-size:13px;display:flex;align-items:center;justify-content:center;text-transform:uppercase}
.btn-line{position:absolute;border:2px solid var(--cyan);color:var(--cyan);font-weight:600;font-size:15px;display:flex;align-items:center;justify-content:center;text-transform:uppercase;background:#fff}
.accent{color:var(--cyan)}
.rule{position:absolute;height:4px;background:var(--cyan)}

/* header / hero */
.hero{position:absolute;left:0;top:0;width:1200px;height:726px}
.brand{position:absolute;left:132px;top:28px;color:#fff;font-family:"Orbitron",sans-serif;font-weight:900;font-size:26px;display:flex;align-items:center;gap:10px}
.brand .mark{width:20px;height:20px;background:var(--cyan)}
.nav{position:absolute;top:36px;color:#fff;font-size:14px;font-weight:500;white-space:nowrap}
.nav.active{font-weight:700}
.hero-kicker{left:129px;top:232px;color:#fff;font-family:"Montserrat",sans-serif;font-size:28px;letter-spacing:3px;font-weight:400}
.hero-title{left:129px;font-family:"Orbitron",sans-serif;font-weight:900;font-size:40px;line-height:1;color:#fff;letter-spacing:1px}
.hero-btn{left:142px;top:433px;width:181px;height:53px;border:2px solid rgba(255,255,255,.75);color:#fff;font-weight:600;font-size:15px;display:flex;align-items:center;justify-content:center}

/* section titles */
.section-title{position:absolute;left:0;width:1200px;text-align:center;font-family:"Orbitron",sans-serif;font-weight:700;font-size:33px;color:var(--navy);letter-spacing:1px}

/* program cards */
.card{position:absolute;background:#fff;box-shadow:0 6px 24px rgba(15,39,64,.12)}
.card h3{position:absolute;left:0;width:100%;text-align:center;font-family:"Orbitron",sans-serif;font-weight:500;font-size:17px;color:var(--navy);letter-spacing:1px}
.card p{position:absolute;left:22px;right:22px;text-align:center;font-size:12px;line-height:19px;color:var(--muted)}

/* tournaments */
.t-card{position:absolute;overflow:hidden}
.t-card .cap{position:absolute;left:0;width:100%;text-align:center;color:#fff}
.t-card .cap h4{font-family:"Roboto Condensed",sans-serif;font-size:21px}
.t-card .cap a{font-size:12px;color:#dfe9f3;text-decoration:underline;letter-spacing:1px}

/* news */
.news{position:absolute;background:#fff;border:1px solid #cfd9e3}
.news .date{position:absolute;color:var(--cyan);font-size:11px;font-weight:600}
.news h5{position:absolute;font-size:17px;font-weight:700;color:var(--navy)}
.news p{position:absolute;font-size:12px;line-height:19px;color:var(--muted)}

/* footer */
.footer{position:absolute;left:0;top:3865px;width:1200px;height:378px;background:var(--navy)}
.footer .bar{position:absolute;left:0;bottom:0;width:1200px;height:60px;background:var(--navy-deep)}
.f-head{position:absolute;color:#fff;font-family:"Orbitron",sans-serif;font-size:13px;font-weight:500;letter-spacing:1px}
.f-link{position:absolute;color:#c9d6e3;font-size:12px}
.f-sep{position:absolute;width:1px;background:#2b4766}
.f-bar-accent{position:absolute;width:3px;height:20px;background:var(--cyan)}
</style>
</head>
<body>

<!-- HERO -->
<div class="hero">
  <svg class="abs" style="left:0;top:0" width="1200" height="726" viewBox="0 0 1200 726">
    <defs>
      <linearGradient id="heroBg" x1="0" y1="0" x2="1" y2="0.6">
        <stop offset="0" stop-color="#143a5e"/>
        <stop offset="0.55" stop-color="#2c5a82"/>
        <stop offset="1" stop-color="#9db6cc"/>
      </linearGradient>
    </defs>
    <polygon points="0,0 1200,0 1200,631 0,726" fill="url(#heroBg)"/>
    <polygon points="700,700 1200,631 1200,726 0,726 0,726" fill="#ffffff"/>
    <polygon points="700,702 1200,631 1200,726" fill="#2ab7ee"/>
  </svg>
  <div class="photo" role="img" aria-label="Two hockey players racing for the puck on the ice under arena lights" style="left:560px;top:120px;width:600px;height:520px;background:radial-gradient(ellipse at 50% 45%,rgba(230,238,246,.55),rgba(120,150,180,.15) 60%,transparent 75%)"></div>
  <div class="brand"><span class="mark"></span>BRAVERIDGE</div>
  <div class="nav active" style="left:417px">SPRING PROGRAM</div>
  <div class="nav" style="left:593px">SUMMER PROGRAM</div>
  <div class="nav" style="left:775px">WINTER</div>
  <div class="nav" style="left:878px">TOURNAMENT</div>
  <div class="nav" style="left:1023px">CONTACT</div>
  <svg class="abs" style="left:34px;top:315px" width="24" height="46" viewBox="0 0 24 46"><polyline points="20,3 4,23 20,43" fill="none" stroke="#fff" stroke-width="5"/></svg>
  <svg class="abs" style="left:1146px;top:315px" width="24" height="46" viewBox="0 0 24 46"><polyline points="4,3 20,23 4,43" fill="none" stroke="#fff" stroke-width="5"/></svg>
  <div class="abs hero-kicker">WELCOME TO</div>
  <div class="abs hero-title" style="top:276px;color:var(--cyan)">BRAVERIDGE HOCKEY</div>
  <div class="abs hero-title" style="top:322px">DEVELOPMENT</div>
  <div class="abs hero-title" style="top:368px">PROGRAMS</div>
  <div class="abs hero-btn">VIEW PROGRAM</div>
  <svg class="abs" style="left:583px;top:585px" width="24" height="36" viewBox="0 0 24 36"><line x1="12" y1="2" x2="12" y2="32" stroke="#fff" stroke-width="2"/><polyline points="3,23 12,33 21,23" fill="none" stroke="#fff" stroke-width="2"/></svg>
</div>

<!-- SPRING PROGRAMS -->
<div class="abs" style="left:0;top:726px;width:1200px;height:700px;background:linear-gradient(180deg,#ffffff 0%,#f3f7fb 40%,#dde7f0 100%)"></div>
<div class="section-title" style="top:758px"><span class="accent">SPIRNG</span> PROGRAMS</div>
<div class="rule" style="left:575px;top:801px;width:50px"></div>
<svg class="abs" style="left:84px;top:1046px" width="22" height="40" viewBox="0 0 22 40"><polyline points="18,3 4,20 18,37" fill="none" stroke="var(--cyan)" stroke-width="5"/></svg>
<svg class="abs" style="left:1144px;top:1046px" width="22" height="40" viewBox="0 0 22 40"><polyline points="4,3 18,20 4,37" fill="none" stroke="var(--cyan)" stroke-width="5"/></svg>

<div class="card" style="left:135px;top:877px;width:302px;height:392px">
  <div class="photo" role="img" aria-label="Hockey player skating fast with ice spray in a dark arena" style="left:0;top:0;width:302px;height:206px;background:linear-gradient(135deg,#0b1c3a,#1f4f8f 60%,#6fa8d8)"></div>
  <h3 style="top:228px">LOREM TOURNAMENT</h3>
  <p style="top:257px">Lorem ipsum dolor sit amet, consectetur adipiscing elit, sed do eiusmod tempor incididunt ut labore et dolore</p>
  <div class="btn-solid" style="left:87px;top:334px;width:129px;height:37px">Learn More</div>
</div>
<div class="card" style="left:783px;top:877px;width:310px;height:392px">
  <div class="photo" role="img" aria-label="Youth hockey game in progress on an indoor rink" style="left:0;top:0;width:310px;height:206px;background:linear-gradient(160deg,#0e2038,#3b5d80 55%,#b7c9da)"></div>
  <h3 style="top:228px">LOREM TOURNAMENT</h3>
  <p style="top:257px">Lorem ipsum dolor sit amet, consectetur adipiscing elit, sed do eiusmod tempor incididunt ut labore et dolore</p>
  <div class="btn-solid" style="left:87px;top:334px;width:129px;height:37px">Learn More</div>
</div>
<div class="card" style="left:437px;top:847px;width:346px;height:455px;border-bottom:5px solid var(--cyan);box-shadow:0 10px 34px rgba(15,39,64,.2)">
  <div class="photo" role="img" aria-label="Hockey player raising a championship trophy" style="left:0;top:0;width:346px;height:241px;background:linear-gradient(150deg,#1b2f6b,#5b73b8 45%,#c8d3e6)"></div>
  <h3 style="top:270px;font-size:18px">LOREM TOURNAMENT</h3>
  <p style="top:304px;font-size:13px;line-height:21px">Lorem ipsum dolor sit amet, consectetur adipiscing elit, sed do eiusmod tempor incididunt ut labore et dolore</p>
  <div class="btn-solid" style="left:98px;top:389px;width:146px;height:40px;font-size:14px">Learn More</div>
</div>

<!-- LATEST TOURNAMENTS -->
<svg class="abs" style="left:0;top:1330px" width="1200" height="640" viewBox="0 0 1200 640">
  <defs>
    <linearGradient id="darkBg" x1="0" y1="0" x2="1" y2="0">
      <stop offset="0" stop-color="#112a45"/>
      <stop offset="1" stop-color="#1c3a5a"/>
    </linearGradient>
  </defs>
  <polygon points="0,142 1200,5 1200,483 0,615" fill="url(#darkBg)"/>
  <polygon points="0,41 520,82 0,142" fill="#2ab7ee"/>
</svg>
<div class="section-title" style="top:1496px;color:#fff;font-size:36px">LATEST TOURNAMENTS</div>
<div class="rule" style="left:553px;top:1543px;width:72px;background:var(--cyan)"></div>
<div class="abs" style="left:0;top:1566px;width:1200px;text-align:center;color:#d6e2ee;font-size:18px">Lorem ipsum dolor sit amet, consectetur adipiscing elit sed do eiusmod tempor</div>

<div class="t-card" style="left:97px;top:1660px;width:330px;height:326px">
  <div class="photo" role="img" aria-label="Two youth hockey players battling for the puck" style="left:0;top:0;width:330px;height:326px;background:linear-gradient(160deg,#7fa8c8,#3f6688 55%,#1b3550)"></div>
  <div class="cap" style="top:255px"><h4>LOREM IPSUM DOLOR SIT</h4><a>VIEW DETAILS</a></div>
</div>
<div class="t-card" style="left:437px;top:1640px;width:329px;height:374px;background:#173a60;border-bottom:5px solid var(--cyan)">
  <div class="photo" role="img" aria-label="Faint photo of an empty hockey arena" style="left:0;top:0;width:329px;height:369px;background:linear-gradient(180deg,#1a3d63,#234f7a 60%,#2d6290)"></div>
  <div class="cap" style="top:92px"><h4 style="font-size:21px">SED UT PERSPICIATIS</h4></div>
  <div class="cap" style="top:132px;left:50px;width:229px;font-size:13px;line-height:21px;color:#b9c9d9">Lorem ipsum dolor sit amet, consectetur adipiscing elit, sed do eiusmod tempor incididunt ut labore et dolore magna</div>
  <div class="cap" style="top:245px;font-size:12px;font-weight:600;letter-spacing:1px">VIEW MORE DETAIL</div>
  <svg class="abs" style="left:208px;top:275px" width="26" height="30" viewBox="0 0 26 30"><path d="M8 28 L4 16 Q3 13 6 14 L9 18 L9 4 Q9 1 11.5 1 Q14 1 14 4 L14 11 L21 12 Q24 13 23 17 L21 28 Z" fill="none" stroke="#fff" stroke-width="1.6"/></svg>
</div>
<div class="t-card" style="left:778px;top:1660px;width:329px;height:326px">
  <div class="photo" role="img" aria-label="Hockey player in white jersey skating with the puck" style="left:0;top:0;width:329px;height:326px;background:linear-gradient(160deg,#b8cde0,#5a82a8 55%,#2a4868)"></div>
  <div class="cap" style="top:260px"><h4>LOREM IPSUM DOLOR SIT</h4><a>VIEW DETAILS</a></div>
</div>

<!-- SUMMER PROGRAM -->
<div class="abs" style="left:109px;top:2104px;width:481px;height:368px;border:5px solid var(--cyan)"></div>
<div class="photo" role="img" aria-label="Hockey player skating with stick in a misty white background" style="left:124px;top:2124px;width:515px;height:393px;background:radial-gradient(ellipse at 50% 50%,#f4f6f8,#c9d2da 70%,#9aa7b3)"></div>
<div class="abs" style="left:582px;top:2179px;width:519px;height:366px;background:#fff;box-shadow:0 8px 30px rgba(15,39,64,.12)"></div>
<div class="abs display" style="left:644px;top:2236px;font-size:31px;color:var(--navy)"><span class="accent">SUMMER</span> PROGRAM</div>
<div class="rule" style="left:644px;top:2278px;width:66px;height:3px"></div>
<div class="abs" style="left:644px;top:2300px;width:400px;font-size:16px;line-height:27px;color:var(--text)">Lorem ipsum dolor sit amet, consectetur adipiscing elit, sed do eiusmod tempor incididunt ut labore et dolore magna aliqua. Ut enim ad minim veniam, quis nostrud exercitation ullam</div>
<div class="btn-line" style="left:649px;top:2434px;width:183px;height:51px">View Program</div>

<!-- WINTER PROGRAMS -->
<svg class="abs" style="left:0;top:2642px" width="1200" height="564" viewBox="0 0 1200 564">
  <defs>
    <linearGradient id="winterBg" x1="0" y1="1" x2="1" y2="0">
      <stop offset="0" stop-color="#0f3556"/>
      <stop offset="0.55" stop-color="#1f8fcf"/>
      <stop offset="1" stop-color="#33c3f3"/>
    </linearGradient>
  </defs>
  <rect width="1200" height="564" fill="url(#winterBg)"/>
</svg>
<div class="photo" role="img" aria-label="Two hockey players facing off over the puck at center ice" style="left:514px;top:2642px;width:686px;height:564px;clip-path:polygon(211px 0,686px 0,686px 564px,0 564px);background:linear-gradient(160deg,#1c2d45,#3c5474 45%,#c9d7e4 85%,#e9eff5)"></div>
<div class="abs display" style="left:46px;top:3060px;transform:rotate(-90deg);transform-origin:0 0;font-size:72px;font-weight:900;color:rgba(255,255,255,.08);letter-spacing:4px">WINTER</div>
<div class="abs display" style="left:127px;top:2748px;font-size:35px;line-height:38px;color:#fff">WINTER<br>PROGRAMS</div>
<div class="abs" style="left:127px;top:2836px;width:74px;height:3px;background:#fff"></div>
<div class="abs" style="left:128px;top:2856px;width:380px;font-size:16px;line-height:27px;color:#e8f3fb">Lorem ipsum dolor sit amet, consectetur adipiscing elit, sed do eiusmod tempor incididunt ut labore et dolore magna aliqua. Ut enim ad minim veniam, quis nostrud exercitation ullamco laboris nisi ut aliquip ex ea</div>
<div class="abs" style="left:153px;top:3025px;color:#fff;font-weight:600;font-size:15px">VIEW PROGRAM</div>

<!-- LATEST NEWS -->
<div class="abs" style="left:0;top:3206px;width:1200px;height:659px;background:#fff"></div>
<div class="section-title" style="top:3260px"><span class="accent">LATEST</span> NEWS</div>
<div class="rule" style="left:575px;top:3302px;width:50px;height:3px"></div>

<div class="news" style="left:109px;top:3349px;width:514px;height:412px">
  <div class="photo" role="img" aria-label="Hockey players competing during a game" style="left:0;top:0;width:512px;height:265px;background:linear-gradient(160deg,#7e95ab,#c3d1de 55%,#e6edf3)"></div>
  <div class="date" style="left:28px;top:288px">25 AUG 2022</div>
  <h5 style="left:28px;top:306px">SPRING HOCKEY PROGRAM</h5>
  <p style="left:28px;top:332px;font-size:13px">Lorem ipsum dolor sit amet, consectetur adipiscing elit sed do eiusmod</p>
  <div class="btn-solid" style="left:28px;top:362px;width:105px;height:30px;font-size:10px">Learn More</div>
</div>
<div class="news" style="left:636px;top:3349px;width:486px;height:199px">
  <div class="photo" role="img" aria-label="Hockey player in red skating on the rink" style="left:0;top:0;width:251px;height:197px;background:linear-gradient(160deg,#1a2536,#4d5f76 55%,#b9c6d3)"></div>
  <div class="date" style="left:280px;top:30px">25 AUG 2022</div>
  <h5 style="left:280px;top:48px">SPRING HOCKEY</h5>
  <p style="left:280px;top:74px;width:180px;font-size:11px;line-height:19px">Lorem ipsum dolor sit amet, consectetur adipiscing elit, sed do eiusmod</p>
  <div class="btn-solid" style="left:280px;top:140px;width:107px;height:29px;font-size:10px">Learn More</div>
</div>
<div class="news" style="left:636px;top:3560px;width:486px;height:201px">
  <div class="photo" role="img" aria-label="Close view of hockey players in red jerseys" style="left:0;top:0;width:251px;height:199px;background:linear-gradient(160deg,#11182a,#5b2a36 50%,#8e96a6)"></div>
  <div class="date" style="left:280px;top:30px">25 AUG 2022</div>
  <h5 style="left:280px;top:48px">SPRING HOCKEY</h5>
  <p style="left:280px;top:74px;width:180px;font-size:11px;line-height:19px">Lorem ipsum dolor sit amet, consectetur adipiscing elit, sed do eiusmod</p>
  <div class="btn-solid" style="left:280px;top:142px;width:107px;height:29px;font-size:10px">Learn More</div>
</div>

<!-- FOOTER -->
<div class="footer">
  <div class="abs" style="left:135px;top:80px;color:#fff;font-family:'Orbitron',sans-serif;font-weight:900;font-size:19px;line-height:24px">BRAVERIDGE<br>HOCKEY<br>DEVELOPMENT</div>
  <div class="abs" style="left:135px;top:176px;width:270px;font-size:12px;line-height:20px;color:#b3c3d3">Lorem ipsum dolor sit amet, consectetur adipiscing elit, sed do eiusmod te</div>

  <div class="f-sep" style="left:475px;top:33px;height:206px"></div>
  <div class="f-bar-accent" style="left:475px;top:84px"></div>
  <div class="f-head" style="left:498px;top:86px">NAVIGATION</div>
  <div class="f-link" style="left:498px;top:118px">Home</div>
  <div class="f-link" style="left:498px;top:148px">Spring Program</div>
  <div class="f-link" style="left:498px;top:177px">Summer Programs</div>
  <div class="f-link" style="left:498px;top:207px">Tournaments</div>

  <div class="f-sep" style="left:699px;top:33px;height:206px"></div>
  <div class="f-bar-accent" style="left:699px;top:86px"></div>
  <div class="f-head" style="left:715px;top:88px">RESOURCES</div>
  <div class="f-link" style="left:715px;top:123px">Winter</div>
  <div class="f-link" style="left:715px;top:153px">Blogs</div>
  <div class="f-link" style="left:715px;top:182px">Contact Us</div>

  <div class="f-sep" style="left:893px;top:33px;height:206px"></div>
  <div class="f-bar-accent" style="left:893px;top:86px"></div>
  <div class="f-head" style="left:918px;top:88px">FOLLLOW US</div>
  <svg class="abs" style="left:918px;top:112px" width="136" height="30" viewBox="0 0 136 30">
    <circle cx="14" cy="15" r="13" fill="#fff"/>
    <circle cx="49" cy="15" r="13" fill="#fff"/>
    <circle cx="84" cy="15" r="13" fill="#fff"/>
    <circle cx="119" cy="15" r="13" fill="#fff"/>
  </svg>

  <div class="bar"></div>
  <div class="abs" style="left:0;top:339px;width:1200px;text-align:center;font-size:11px;color:#c9d6e3">© 2022 <span style="text-decoration:underline">Braveridge Hockey Development</span> All Rights Reserved</div>
</div>

</body>
</html>
```